product development company PEVRANOX LLC business card

We need a business card design for a company based in Texas called 'PEVRANOX LLC'. Our first product is a illuminated portable ice chest that is called ' Ember Ridge coolers'. Ember ridge coolers is trademarked. I would like to have the ember ridge trademark somewhere on the card as well as the PEVRANOX LLC name.

Target Market(s)

outdoor industry

Industry/Entity Type

Business

Contact Information for Business Card

i would like to have PEVRANOX LLC logo larger than the Ember ridge coolers logo.

Font styles to use
Serif
Sans Serif

```html
<!DOCTYPE html>
<html lang="en">
<head>
<meta charset="utf-8">
<title>PEVRANOX LLC – Business Card</title>
<link rel="stylesheet" href="https://fonts.googleapis.com/css2?family=Open+Sans:wght@400;700&display=swap">
<style>
  :root {
    --backdrop: #e9e6e2;
    --card: #ffffff;
    --ink: #111111;
    --band: #0d0d0d;
  }
  * { box-sizing: border-box; margin: 0; padding: 0; }
  html, body {
    width: 1200px; height: 1000px; overflow: hidden;
    background: var(--backdrop);
    font-family: "Open Sans", Arial, sans-serif;
    color: var(--ink);
  }
  .business-card {
    position: absolute; left: 100px; top: 203px;
    width: 1000px; height: 594px;
    background: var(--card);
    box-shadow: 0 6px 18px rgba(0,0,0,0.18);
    overflow: hidden;
  }
  .company-mark {
    position: absolute; left: 50px; top: 62px;
    text-align: center; font-weight: 700; line-height: 1;
  }
  .company-mark .company-name { display: block; font-size: 62px; letter-spacing: 3px; }
  .company-mark .company-suffix { display: block; font-size: 30px; letter-spacing: 12px; margin-top: 10px; }
  .person {
    position: absolute; left: 50px; top: 262px;
  }
  .person-name { font-size: 31px; font-weight: 700; line-height: 1.2; }
  .person-title { font-size: 23px; font-weight: 400; line-height: 1.2; }
  .contact-list {
    position: absolute; left: 50px; top: 356px;
    list-style: none; font-size: 23px; line-height: 34px;
  }
  .contact-list li { display: flex; align-items: center; gap: 10px; }
  .contact-list li.address { margin-top: 6px; }
  .contact-list svg { width: 20px; height: 22px; flex: none; fill: var(--ink); }
  .product-mark {
    position: absolute; right: 52px; top: 468px;
    display: flex; align-items: center; gap: 12px;
    font-size: 34px; font-weight: 700; line-height: 1;
  }
  .product-mark .mark-square { width: 30px; height: 30px; background: var(--ink); }
  .card-band { position: absolute; left: 0; bottom: 0; width: 1000px; height: 20px; }
  .card-band polygon { fill: var(--band); }
</style>
</head>
<body>
  <div class="business-card">
    <div class="company-mark">
      <span class="company-name">PEVRANOX</span>
      <span class="company-suffix">LLC</span>
    </div>

    <div class="person">
      <p class="person-name">MARCUS VELLAN</p>
      <p class="person-title">Managing Director</p>
    </div>

    <ul class="contact-list">
      <li>
        <svg viewBox="0 0 20 22" aria-hidden="true"><path d="M5 1h10a2 2 0 0 1 2 2v16a2 2 0 0 1-2 2H5a2 2 0 0 1-2-2V3a2 2 0 0 1 2-2zm1 3v10h8V4zm4 12a1.5 1.5 0 1 0 0 3 1.5 1.5 0 0 0 0-3z"/></svg>
        + 000 000 0000
      </li>
      <li>
        <svg viewBox="0 0 20 22" aria-hidden="true"><path d="M1 8c0-3 4-5 9-5s9 2 9 5v2h-5V8H6v2H1zm3 4h12l2 7H2z"/></svg>
        + 000 000 0000
      </li>
      <li>
        <svg viewBox="0 0 20 22" aria-hidden="true"><path d="M1 5h18v12H1zm1.5 1.5L10 12l7.5-5.5V6h-15z"/></svg>
        info@pevranoxemberridge.com
      </li>
      <li>
        <svg viewBox="0 0 20 22" aria-hidden="true"><path d="M10 2a9 9 0 1 0 0 18 9 9 0 0 0 0-18zm0 2c1 0 2 2 2.4 5H7.6C8 6 9 4 10 4zM4.2 9h2A14 14 0 0 1 7 5a7 7 0 0 0-2.8 4zm9.6 0h2A7 7 0 0 0 13 5a14 14 0 0 1 .8 4zM4.2 13a7 7 0 0 0 2.8 4 14 14 0 0 1-.8-4zm3.4 0c.4 3 1.4 5 2.4 5s2-2 2.4-5zm6.2 0a14 14 0 0 1-.8 4 7 7 0 0 0 2.8-4z"/></svg>
        www.pevranoxemberridge.com
      </li>
      <li class="address">
        <svg viewBox="0 0 20 22" aria-hidden="true"><path d="M10 1a7 7 0 0 0-7 7c0 5 7 13 7 13s7-8 7-13a7 7 0 0 0-7-7zm0 4a3 3 0 1 1 0 6 3 3 0 0 1 0-6z"/></svg>
        2716 N. Mesa Ln. Harlow, TX 78290
      </li>
    </ul>

    <div class="product-mark">
      <span class="mark-square"></span>
      <span class="product-name">Ember Ridge</span>
    </div>

    <svg class="card-band" viewBox="0 0 1000 20" preserveAspectRatio="none" aria-hidden="true">
      <polygon points="0,2 538,2 556,20 0,20"/>
      <polygon points="574,9 1000,9 1000,20 586,20"/>
    </svg>
  </div>
</body>
</html>
```